Business Card Design

I am a Building Surveyor and run my own Building Consultat company, providing professional advice and services to builders, architects, designers, owners, etc.

Industry/Entity Type

Business

Contact Information for Business Card

Dorwen Fasque BBldgSurv (Hons)
Managing Director

47 Marlow Crest, Kelvoth Downs WA 6158
Mobile 0498 153 607
Email Dorwen.fasque@ridgeplumbav.com

Requirements
Must have
• I would like the back of the business card to be one colour (a shade of either black or maroon, matching the colours of my logo). Positioned in the centre on the back of the business card is to be my logo.

The front of the card is to be white, with my contact information in either black or maroon. The ADBldgSurv after my name should be in a smaller font size than my name. I would also like a small logo somewhere on this side of the card.

```html
<!DOCTYPE html>
<html lang="en">
<head>
<meta charset="utf-8">
<title>Ridgeform Building Consultants – Business Card</title>
<link rel="stylesheet" href="https://fonts.googleapis.com/css2?family=Cinzel:wght@400&family=Source+Sans+3:wght@400;700&display=swap">
<style>
  :root {
    --backdrop-center: #f7f8f9;
    --backdrop-edge: #dde3e6;
    --card-dark: #231f20;
    --card-light-center: #f6f6f6;
    --card-light-edge: #b8b9bb;
    --maroon: #6d1a12;
    --mark-maroon: #7a1f17;
    --logo-grey-dark: #6a6a6a;
    --logo-grey-light: #4b4b4b;
    --text-grey: #4a4a4a;
    --title-grey: #5a5a5a;
  }
  * { margin: 0; padding: 0; box-sizing: border-box; }
  html, body { width: 1200px; height: 1000px; overflow: hidden; }
  body {
    position: relative;
    background: radial-gradient(ellipse at 50% 45%, var(--backdrop-center) 0%, var(--backdrop-center) 35%, var(--backdrop-edge) 100%);
    font-family: "Source Sans 3", "Helvetica Neue", Arial, sans-serif;
  }
  .card {
    position: absolute;
    left: 312px;
    width: 587px;
    height: 362px;
  }
  .card--back { top: 82px; background: var(--card-dark); }
  .card--front {
    top: 531px;
    background: radial-gradient(ellipse at 50% 45%, var(--card-light-center) 0%, #e6e6e7 45%, var(--card-light-edge) 100%);
  }
  .brand {
    position: absolute;
    display: flex;
    align-items: center;
  }
  .brand__dot { border-radius: 50%; background: var(--mark-maroon); flex: none; }
  .brand__name {
    font-family: "Cinzel", "Times New Roman", serif;
    font-weight: 400;
    text-align: center;
    line-height: 1;
    color: var(--logo-grey-dark);
  }
  .brand__sub {
    display: flex;
    align-items: center;
    letter-spacing: 0.06em;
  }
  .brand__sub::before, .brand__sub::after {
    content: "";
    flex: 1;
    height: 1px;
    background: currentColor;
    opacity: 0.6;
  }
  .brand--back { left: 112px; top: 150px; }
  .brand--back .brand__dot { width: 70px; height: 70px; margin-right: 20px; }
  .brand--back .brand__name { font-size: 31px; color: var(--logo-grey-dark); }
  .brand--back .brand__sub { font-size: 11px; gap: 6px; margin-top: 4px; }
  .brand--front { left: 163px; top: 44px; }
  .brand--front .brand__dot { width: 50px; height: 50px; margin-right: 12px; }
  .brand--front .brand__name { font-size: 23px; color: var(--logo-grey-light); }
  .brand--front .brand__sub { font-size: 8px; gap: 4px; margin-top: 3px; }
  .person {
    position: absolute;
    top: 176px;
    width: 100%;
    text-align: center;
  }
  .person__name { font-size: 24px; font-weight: 700; color: var(--maroon); line-height: 1.1; }
  .person__title { font-size: 17px; color: var(--title-grey); line-height: 1.2; }
  .contact {
    position: absolute;
    top: 301px;
    width: 100%;
    text-align: center;
    font-size: 16px;
    line-height: 22px;
    color: var(--text-grey);
    letter-spacing: 0.01em;
  }
  .contact__sep { color: var(--maroon); }
</style>
</head>
<body>
  <section class="card card--back" aria-label="Card back">
    <div class="brand brand--back">
      <span class="brand__dot"></span>
      <div class="brand__name">
        <div>RIDGEFORM</div>
        <div class="brand__sub">BUILDING CONSULTANTS</div>
      </div>
    </div>
  </section>

  <section class="card card--front" aria-label="Card front">
    <div class="brand brand--front">
      <span class="brand__dot"></span>
      <div class="brand__name">
        <div>RIDGEFORM</div>
        <div class="brand__sub">BUILDING CONSULTANTS</div>
      </div>
    </div>
    <div class="person">
      <div class="person__name">Dorwen Fasque</div>
      <div class="person__title">ADBldgSurv</div>
    </div>
    <div class="contact">
      <div>Director 47 Marlow Crest, Kelvoth Downs WA 6158</div>
      <div>Mobile: 0498 153 607 <span class="contact__sep">•</span> Email: Dorwen.fasque@ridgeplumbav.com</div>
    </div>
  </section>
</body>
</html>
```